Our Work

I would like to Upload Pictures and make a flyer showing some of the services we offer. I have attached a sample flyer layout and pictures I would like to use with the services labeled.

```html
<!DOCTYPE html>
<html lang="en">
<head>
<meta charset="utf-8">
<title>Our Services Flyer</title>
<link href="https://fonts.googleapis.com/css2?family=Montserrat:wght@600;700;800&display=swap" rel="stylesheet">
<style>
  :root {
    --page-bg: #e9e6e6;
    --frame-grey: #7e7d7f;
    --panel: #eeedef;
    --brand-blue: #1632c4;
    --brand-blue-dark: #0c1f9a;
    --label-blue: #1a2db8;
    --silver: #b9bcc4;
    --white: #ffffff;
  }
  * { margin: 0; padding: 0; box-sizing: border-box; }
  html, body { width: 1200px; height: 890px; overflow: hidden; background: var(--page-bg); }
  body { position: relative; font-family: "Montserrat", Arial, sans-serif; }

  .flyer-holder { position: absolute; left: 263px; top: 8px; width: 674px; height: 875px; }
  .flyer {
    position: absolute; left: 0; top: 0; width: 613px; height: 795px;
    background: var(--frame-grey);
    transform: scale(1.1); transform-origin: 0 0;
  }
  .panel { position: absolute; left: 20px; top: 22px; width: 573px; height: 721px; background: var(--panel); }
  .overlay { position: absolute; left: 0; top: 0; width: 613px; height: 795px; }

  .title {
    position: absolute; left: 0; width: 613px; top: 23px; text-align: center;
    color: var(--white); font-weight: 700; font-size: 29px; letter-spacing: 0.2px;
  }

  .photo { position: absolute; border: 1px solid #3a3a3a; }
  .photo--house { background: linear-gradient(180deg, #8fb7e0 0%, #c9b8a4 50%, #5d9a3c 85%); }
  .photo--interior { background: linear-gradient(160deg, #d9c8a8 0%, #b89a72 55%, #8a6a48 100%); }
  .photo--scaffold { background: linear-gradient(160deg, #e2d8c8 0%, #a97a4f 60%, #6c4a30 100%); }
  .photo--steps { background: linear-gradient(180deg, #6d8a45 0%, #8a8680 50%, #b8b4ac 100%); }
  .photo--doorway { background: linear-gradient(180deg, #6b5a48 0%, #c9ccd0 45%, #3a4a7a 100%); }
  .photo--siding { background: linear-gradient(180deg, #cfd6dd 0%, #9a968e 60%, #6b6d60 100%); }
  .photo--drywall { background: linear-gradient(90deg, #2a4aa8 0%, #e4e2dc 40%, #d8d4cc 100%); }
  .photo--balcony { background: linear-gradient(180deg, #9fb8d8 0%, #e6e4de 45%, #a8a8a2 100%); }
  .photo--flooring { background: linear-gradient(135deg, #8a4a24 0%, #c99a6a 55%, #d8c6a8 100%); }
  .photo--roof { background: linear-gradient(180deg, #6f9ad4 0%, #c7c6c4 45%, #8a4a32 80%, #4f6a3a 100%); }
  .photo--complex { background: linear-gradient(180deg, #8fb0d8 0%, #e2ddd6 45%, #b8b0a6 80%, #6a7a4a 100%); }

  .label {
    position: absolute; color: var(--label-blue); font-weight: 700;
    font-size: 8.6px; line-height: 12px; white-space: nowrap; letter-spacing: 0.1px;
  }

  .contact {
    position: absolute; top: 761px; color: var(--white); font-weight: 600;
    font-size: 9.2px; line-height: 12px; display: flex; align-items: center; gap: 5px; white-space: nowrap;
  }
  .contact svg { width: 8px; height: 8px; }
</style>
</head>
<body>
<div class="flyer-holder">
  <div class="flyer">
    <div class="panel"></div>

    <svg class="overlay" viewBox="0 0 613 795" aria-hidden="true">
      <polygon points="98,0 104,0 168,86 162,86" fill="var(--brand-blue)"/>
      <polygon points="502,0 508,0 452,86 446,86" fill="var(--brand-blue)"/>
      <polygon points="108,0 498,0 446,80 168,80" fill="var(--silver)"/>
      <polygon points="114,0 490,0 442,76 172,76" fill="var(--brand-blue)"/>
      <rect x="170" y="85" width="272" height="4" fill="var(--brand-blue-dark)"/>

      <g stroke="var(--brand-blue)" stroke-width="1" fill="none">
        <polyline points="222,163 222,267 77,267"/>
        <line x1="222" y1="240" x2="526" y2="240"/>
        <line x1="150" y1="352" x2="150" y2="388"/>
        <line x1="106" y1="388" x2="524" y2="388"/>
        <line x1="193" y1="408" x2="244" y2="408"/>
        <line x1="364" y1="408" x2="418" y2="408"/>
        <line x1="147" y1="502" x2="147" y2="557"/>
        <line x1="68" y1="557" x2="520" y2="557"/>
        <line x1="213" y1="582" x2="262" y2="582"/>
        <line x1="392" y1="582" x2="432" y2="582"/>
        <line x1="147" y1="682" x2="147" y2="719"/>
        <line x1="68" y1="719" x2="520" y2="719"/>
      </g>
      <g fill="var(--brand-blue)">
        <circle cx="222" cy="163" r="1.8"/><circle cx="77" cy="267" r="1.8"/>
        <circle cx="526" cy="240" r="1.8"/><circle cx="150" cy="352" r="1.8"/>
        <circle cx="106" cy="388" r="1.8"/><circle cx="524" cy="388" r="1.8"/>
        <circle cx="193" cy="408" r="1.4"/><circle cx="244" cy="408" r="1.4"/>
        <circle cx="364" cy="408" r="1.4"/><circle cx="418" cy="408" r="1.4"/>
        <circle cx="147" cy="502" r="1.8"/><circle cx="68" cy="557" r="1.8"/>
        <circle cx="520" cy="557" r="1.8"/><circle cx="213" cy="582" r="1.4"/>
        <circle cx="262" cy="582" r="1.4"/><circle cx="392" cy="582" r="1.4"/>
        <circle cx="432" cy="582" r="1.4"/><circle cx="68" cy="719" r="1.8"/>
        <circle cx="520" cy="719" r="1.8"/>
      </g>
    </svg>

    <h1 class="title">OUR SERVICES</h1>

    <div class="photo photo--house" style="left:39px;top:112px;width:154px;height:112px" role="img" aria-label="Photo of a painted two-storey house with lawn"></div>
    <div class="photo photo--interior" style="left:250px;top:113px;width:154px;height:111px" role="img" aria-label="Photo of interior painting with scaffolding in a stairwell"></div>
    <div class="photo photo--scaffold" style="left:418px;top:113px;width:154px;height:112px" role="img" aria-label="Photo of scaffolding and drop cloths in a living room"></div>
    <div class="photo photo--steps" style="left:250px;top:258px;width:154px;height:54px" role="img" aria-label="Photo of concrete steps being repaired"></div>
    <div class="photo photo--doorway" style="left:418px;top:258px;width:154px;height:119px" role="img" aria-label="Photo of crew installing a patio door"></div>
    <div class="photo photo--siding" style="left:250px;top:322px;width:154px;height:55px" role="img" aria-label="Photo of siding work on an apartment building"></div>
    <div class="photo photo--drywall" style="left:250px;top:424px;width:154px;height:56px" role="img" aria-label="Photo of drywall installation in a room"></div>
    <div class="photo photo--balcony" style="left:418px;top:424px;width:154px;height:123px" role="img" aria-label="Photo of balcony rehab on a multi-storey building"></div>
    <div class="photo photo--flooring" style="left:250px;top:488px;width:154px;height:59px" role="img" aria-label="Photo of hardwood flooring being laid"></div>
    <div class="photo photo--roof" style="left:250px;top:596px;width:155px;height:111px" role="img" aria-label="Photo of roof and facade repairs on a townhouse"></div>
    <div class="photo photo--complex" style="left:418px;top:596px;width:154px;height:111px" role="img" aria-label="Photo of an apartment complex after stucco repairs"></div>

    <span class="label" style="left:39px;top:231px">EXTERIOR &amp; INTERIOR PAINTING</span>
    <span class="label" style="left:36px;top:277px">GENERAL CARPENTRY</span>
    <span class="label" style="left:156px;top:276px">FRAMING REPAIRS</span>
    <span class="label" style="left:54px;top:296px">SIDING/GUTTERS /WINDOWS/DOORS</span>
    <span class="label" style="left:61px;top:335px">CONCRETE WALKWAYS/STOOPS</span>
    <span class="label" style="left:36px;top:368px">BALCONY/DECK</span>
    <span class="label" style="left:57px;top:381px">/REHAB</span>
    <span class="label" style="left:158px;top:370px">TUCKPOINTING</span>
    <span class="label" style="left:85px;top:402px">SEALANTS/CAULKS</span>
    <span class="label" style="left:248px;top:402px">PRESSURE WASHING</span>
    <span class="label" style="left:423px;top:402px">SPECIALTY COATINGS</span>
    <span class="label" style="left:79px;top:439px">DEYWALL INSTALL/REPAIR</span>
    <span class="label" style="left:36px;top:461px">PLASTERS REPAIRS</span>
    <span class="label" style="left:137px;top:460px">WALLPAPER REMOVAL</span>
    <span class="label" style="left:36px;top:484px">FLOORING/TILE/CARPET/HARDWOOD/VINYL</span>
    <span class="label" style="left:65px;top:564px">LEAK INVESTIGATIONS:</span>
    <span class="label" style="left:36px;top:576px">-FACADES,ROOFS,INTERIOR LEAKS</span>
    <span class="label" style="left:270px;top:576px">EIFS/STUCCO REPAIRS</span>
    <span class="label" style="left:439px;top:576px">PLUMBING REPAIRS</span>
    <span class="label" style="left:95px;top:622px">ROFFING REPAIRS</span>
    <span class="label" style="left:74px;top:642px">LEAD SAFE RENOVATIONS</span>
    <span class="label" style="left:87px;top:664px">SPECIALTY COATINGS</span>

    <div class="contact" style="left:48px">
      <svg viewBox="0 0 10 10" aria-hidden="true"><circle cx="5" cy="5" r="4.2" fill="none" stroke="#fff" stroke-width="1"/><ellipse cx="5" cy="5" rx="1.8" ry="4.2" fill="none" stroke="#fff" stroke-width="0.8"/><line x1="0.8" y1="5" x2="9.2" y2="5" stroke="#fff" stroke-width="0.8"/></svg>
      <span>northgatecontracting.com</span>
    </div>
    <div class="contact" style="left:254px">
      <svg viewBox="0 0 10 10" aria-hidden="true"><path d="M2.2 0.8 L3.8 3 L2.8 4 Q4 6.2 6 7.2 L7 6.2 L9.2 7.8 L8.2 9.2 Q3.5 9 0.8 1.8 Z" fill="#fff"/></svg>
      <span>555.214.0386</span>
    </div>
    <div class="contact" style="left:406px">
      <svg viewBox="0 0 12 10" style="width:10px" aria-hidden="true"><rect x="0.5" y="1.5" width="11" height="7" fill="none" stroke="#fff" stroke-width="1"/><polyline points="0.5,1.5 6,5.5 11.5,1.5" fill="none" stroke="#fff" stroke-width="1"/></svg>
      <span>info@northgatecontracting.com</span>
    </div>
  </div>
</div>
</body>
</html>
```